Iconic Australian Wine Brand looking for a complete brand makeover

- Require a new label design for the Clover Ridge range of wines
- Complete brand makeover with refreshed packaging design
- Inspiration for consumers to see the brand in a new light
- The final design should communicate fun, energetic and modern packaging with the aim of engaging our core target market of 20 - 35 year old female wine drinkers, while re-engaging our loyal female demographic of 35+ year olds.

Target Market(s)

Engage a Core target market of 20-35 year old female wine drinkers / secondary target market: re-engage our loyal female demographic of 35+ year olds

Requirements
Must have
• Complete brand makeover in order to re-engage our loyal female drinkers, now in their mid to late 30's
Nice to have
• Play on words for the Brand name

```html
<!DOCTYPE html>
<html lang="en">
<head>
<meta charset="utf-8">
<title>Clover Ridge – Label Range</title>
<link rel="stylesheet" href="https://fonts.googleapis.com/css2?family=Quicksand:wght@400;500&display=swap">
<style>
  :root {
    --canvas-bg: #ffffff;
    --white: #ffffff;
    --red-sash: #e30613;
    --sauv-ground: #f29100;
    --sauv-band: #662482;
    --sauv-accent: #e6177a;
    --merlot-ground: #14a39a;
    --merlot-band: #dcdc00;
    --merlot-accent: #1470b8;
  }
  html, body {
    margin: 0;
    padding: 0;
    overflow: hidden;
    background: var(--canvas-bg);
  }
  .canvas {
    position: relative;
    width: 1200px;
    height: 1000px;
    background: var(--canvas-bg);
    overflow: hidden;
    font-family: "Quicksand", sans-serif;
  }
  .label {
    position: absolute;
    top: 251px;
    width: 236px;
    height: 496px;
    display: block;
  }
  .label--sauvignon { left: 323px; }
  .label--merlot { left: 659px; }
  .brand-name { font-family: "Quicksand", sans-serif; font-weight: 400; font-size: 29px; fill: var(--white); }
  .region { font-family: "Quicksand", sans-serif; font-weight: 400; font-size: 11px; letter-spacing: 3.2px; fill: var(--white); }
  .varietal { font-family: "Quicksand", sans-serif; font-weight: 500; font-size: 15px; }
  .origin { font-family: "Quicksand", sans-serif; font-weight: 500; font-size: 7px; fill: var(--white); }
</style>
</head>
<body>
<main class="canvas">

  <svg class="label label--sauvignon" viewBox="0 0 236 496" aria-label="Clover Ridge Sauvignon Blanc label">
    <rect class="ground" width="236" height="496" fill="var(--sauv-ground)"/>
    <rect class="accent-band" x="126" y="23" width="23" height="473" fill="var(--sauv-accent)"/>
    <rect class="main-band" x="77" y="0" width="49" height="407" fill="var(--sauv-band)"/>
    <polygon class="sash" points="0,254 236,119 236,186 0,321" fill="var(--red-sash)"/>
    <rect class="figure-mark" x="80" y="164" width="70" height="108" rx="6" fill="var(--sauv-ground)" role="img" aria-label="Silhouettes of four standing women"/>
    <text class="brand-name" x="30" y="91">Clover Ridge</text>
    <text class="region" x="32" y="105">Central Victoria</text>
    <text class="varietal" x="118" y="449" text-anchor="middle" fill="var(--sauv-band)">Sauvignon Blanc</text>
    <text class="origin" x="117" y="481" text-anchor="middle">Wine of Australia</text>
  </svg>

  <svg class="label label--merlot" viewBox="0 0 236 496" aria-label="Clover Ridge Merlot label">
    <rect class="ground" width="236" height="496" fill="var(--merlot-ground)"/>
    <rect class="accent-band" x="126" y="23" width="23" height="473" fill="var(--merlot-accent)"/>
    <rect class="main-band" x="77" y="0" width="49" height="407" fill="var(--merlot-band)"/>
    <polygon class="sash" points="0,254 236,119 236,186 0,321" fill="var(--red-sash)"/>
    <rect class="figure-mark" x="80" y="164" width="70" height="108" rx="6" fill="var(--merlot-ground)" role="img" aria-label="Silhouettes of four standing women"/>
    <text class="brand-name" x="30" y="91">Clover Ridge</text>
    <text class="region" x="32" y="105">Central Victoria</text>
    <text class="varietal" x="118" y="449" text-anchor="middle" fill="var(--white)">Merlot</text>
    <text class="origin" x="117" y="481" text-anchor="middle">Wine of Australia</text>
  </svg>

</main>
</body>
</html>
```